Banner Design for High End Jewelry Website

We need a banner for our website (brindlestone.com) for a sale that we will be running. The banner should be a size 1187 × 400. I have included a few pieces of jewelry to be included in the banner (do not need to use all, can use just some). The banner should say:
"Christmas is Closer Than You Think Sale!"
Shop Now

Industry/Entity Type

Jewelry

```html
<!DOCTYPE html>
<html lang="en">
<head>
<meta charset="utf-8">
<title>Christmas Sale Banner</title>
<link rel="stylesheet" href="https://fonts.googleapis.com/css2?family=Great+Vibes&family=Playfair+Display:wght@400&family=Cinzel:wght@400&display=swap">
<style>
  :root {
    --silver-light: #f7f7f7;
    --silver-mid: #dcdcdc;
    --gold-script: #8a7612;
    --headline-grey: #555555;
    --button-gold: #7f6e0f;
    --button-text: #ffffff;
    --ornament-dark: #8a8a8a;
    --jewel-gold: #c9a23a;
    --jewel-deep: #8c6a1e;
  }
  html, body {
    margin: 0;
    padding: 0;
    width: 1200px;
    height: 404px;
    overflow: hidden;
  }
  .banner {
    position: relative;
    width: 1200px;
    height: 404px;
    overflow: hidden;
    background:
      radial-gradient(ellipse at 55% 45%, var(--silver-light) 0%, rgba(247,247,247,0) 60%),
      radial-gradient(circle at 20% 30%, rgba(255,255,255,0.7) 0%, rgba(255,255,255,0) 25%),
      radial-gradient(circle at 85% 70%, rgba(255,255,255,0.6) 0%, rgba(255,255,255,0) 25%),
      linear-gradient(180deg, var(--silver-mid) 0%, var(--silver-light) 50%, var(--silver-mid) 100%);
  }
  .sparkles {
    position: absolute;
    inset: 0;
  }
  .ornaments {
    position: absolute;
    left: 0;
    top: 0;
    width: 270px;
    height: 404px;
    background: radial-gradient(ellipse 50% 50% at 50% 55%, rgba(138,138,138,0.75) 0%, rgba(138,138,138,0.35) 50%, rgba(138,138,138,0) 100%);
  }
  .jewel {
    position: absolute;
    border-radius: 20px;
    background: radial-gradient(circle at 50% 45%, var(--jewel-gold) 0%, var(--jewel-deep) 70%, rgba(140,106,30,0.4) 100%);
    opacity: 0.85;
  }
  .jewel--earrings { left: 985px; top: 12px;  width: 205px; height: 160px; }
  .jewel--brooch   { left: 1015px; top: 178px; width: 150px; height: 90px; }
  .jewel--rings    { left: 928px; top: 300px; width: 272px; height: 104px; }
  .headline-script {
    position: absolute;
    left: 220px;
    top: 58px;
    width: 750px;
    margin: 0;
    text-align: center;
    font-family: "Great Vibes", cursive;
    font-weight: 400;
    font-size: 110px;
    line-height: 1;
    letter-spacing: 2px;
    white-space: nowrap;
    color: var(--gold-script);
  }
  .headline-serif {
    position: absolute;
    left: 280px;
    top: 226px;
    width: 650px;
    margin: 0;
    text-align: center;
    font-family: "Playfair Display", serif;
    font-weight: 400;
    font-size: 56px;
    line-height: 1.2;
    white-space: nowrap;
    color: var(--headline-grey);
  }
  .shop-button {
    position: absolute;
    left: 503px;
    top: 322px;
    width: 194px;
    height: 36px;
    border-radius: 10px;
    background: var(--button-gold);
    color: var(--button-text);
    font-family: "Cinzel", serif;
    font-size: 22px;
    line-height: 36px;
    text-align: center;
    text-decoration: none;
    letter-spacing: 0.5px;
  }
</style>
</head>
<body>
  <div class="banner">
    <svg class="sparkles" width="1200" height="404" viewBox="0 0 1200 404" aria-hidden="true">
      <g fill="#ffffff">
        <circle cx="300" cy="40" r="2"/><circle cx="420" cy="90" r="1.5"/>
        <circle cx="610" cy="30" r="2"/><circle cx="760" cy="70" r="1.5"/>
        <circle cx="880" cy="40" r="2"/><circle cx="350" cy="300" r="1.5"/>
        <circle cx="820" cy="320" r="2"/><circle cx="470" cy="370" r="1.5"/>
        <circle cx="700" cy="385" r="2"/><circle cx="260" cy="200" r="1.5"/>
      </g>
    </svg>

    <div class="ornaments" role="img" aria-label="Silver Christmas baubles hanging from curled streamers"></div>

    <h1 class="headline-script">Christmas is Closer</h1>
    <p class="headline-serif">Than You Think Sale!</p>
    <a class="shop-button" href="#">Shop Now</a>

    <div class="jewel jewel--earrings" role="img" aria-label="Gold earrings with emerald and ruby cabochons and diamonds"></div>
    <div class="jewel jewel--brooch" role="img" aria-label="Gold brooch with a central ruby and small diamonds"></div>
    <div class="jewel jewel--rings" role="img" aria-label="Gold scale-pattern ring and stacked gemstone rings"></div>
  </div>
</body>
</html>
```